Velmaro App for Smart Devices IoT WiFi Electronic

Velmaro is a siren manufacturer. This application is used for the company's products that have a Wi-Fi connection and an internet connection, which can be configured and activated remotely through this application. In addition, this application is used to activate the siren at specific times for the start and end of shifts in companies and schools. Users will be siren installers and IT or HR managers.
In addition to activating motorized sirens timers, some siren models have speakers and allow you to play TTS (text to speech) audio, audio recorded by the user on the phone and upload audio (mp3) with playlist programming with start and end times.
Application screens: home with dashboard (one dashboard for each category). Device categories: timers, speakers, motorized siren. Screen for requesting evaluation in the Play Store. Screen for registering the user profile. Screen for registering devices according to their category (timers, speakers, motorized siren). Screen for registering device groups. Screen for pairing the device on the client's Wi-Fi network. Screen for registering activation times. Screen for uploading MP3 audios. Screen for registering playlists with audio selection, start and end times. Screen for recording audio for later sending to the speakers. Screen for converting text to speech and sending to the speakers. It is important to have a time picker with the day of the week to program the activation times and playlist.

Target Market(s)

Schools, Companies and Stores.

Industry/Entity Type

IoT

Font styles to use
Sans Serif
Other font styles liked:
• roboto

Colors
FFC000
F8CF3A
FAE287
FDF2CF
FEFAEE

Requirements
Must have
• time picker with weekdays for timer programming feature.
Nice to have
• app review request screen on play store

```html
<!DOCTYPE html>
<html lang="en">
<head>
<meta charset="utf-8">
<title>Velmaro – Siren Timer App Screens</title>
<link href="https://fonts.googleapis.com/css2?family=Lato:ital,wght@0,400;0,700;0,900;1,400&family=Roboto:wght@700;900&display=swap" rel="stylesheet">
<style>
  :root{
    --yellow:#ffc000;
    --yellow-soft:#f8cf3a;
    --dark:#333333;
    --ink:#222222;
    --text:#444444;
    --muted:#555555;
    --canvas:#e4e4e4;
    --white:#ffffff;
  }
  html,body{margin:0;padding:0;width:939px;height:1200px;overflow:hidden;background:var(--canvas);}
  body{font-family:"Lato",sans-serif;color:var(--text);}
  .board{position:relative;width:1500px;height:1916px;transform:scale(0.626);transform-origin:0 0;}
  .screen{position:absolute;width:414px;background:var(--white);border-bottom:4px solid var(--yellow);overflow:hidden;}
  .screen--timers{left:77px;top:39px;height:1117px;}
  .screen--schedule{left:543px;top:39px;height:892px;}
  .screen--devices{left:1009px;top:39px;height:892px;}
  .screen--pairing{left:543px;top:981px;height:891px;}

  .app-header{position:absolute;left:0;top:0;width:414px;height:205px;}
  .app-header svg{position:absolute;left:0;top:0;}
  .brand{position:absolute;left:0;right:0;top:14px;text-align:center;font-family:"Lato",sans-serif;font-weight:700;font-size:66px;color:var(--yellow);letter-spacing:1px;}
  .nav-icons{position:absolute;top:111px;left:0;right:0;display:flex;justify-content:center;gap:7px;}
  .nav-icon{width:36px;height:36px;border-radius:50%;background:var(--yellow);display:flex;align-items:center;justify-content:center;}

  .screen-title{position:absolute;left:0;right:0;text-align:center;font-family:"Roboto",sans-serif;font-weight:900;color:var(--ink);text-transform:uppercase;}
  .card{position:absolute;left:33px;width:348px;background:var(--white);border-radius:4px;box-shadow:0 2px 10px rgba(0,0,0,0.07);}
  .abs{position:absolute;}
  .hl{color:var(--yellow);font-weight:700;}
  .toggle{position:absolute;width:18px;height:9px;border:2px solid var(--yellow);border-radius:7px;box-sizing:content-box;}
  .toggle::after{content:"";position:absolute;left:1px;top:1px;width:7px;height:7px;border-radius:50%;background:var(--yellow);}
  .toggle--on{border-color:var(--dark);background:var(--dark);}
  .toggle--on::after{left:auto;right:1px;background:var(--yellow);}

  .schedule-time{position:absolute;left:24px;top:18px;font-size:15px;color:var(--text);}
  .schedule-name{position:absolute;left:23px;font-size:15px;color:var(--text);}
  .field{height:56px;}
  .field-label{position:absolute;left:21px;top:19px;font-size:15px;color:var(--muted);}
  .field-icon{position:absolute;right:20px;top:20px;}
  .btn-primary{position:absolute;left:33px;top:725px;width:348px;height:56px;border-radius:6px;background:var(--yellow);color:var(--white);font-weight:900;font-size:16px;display:flex;align-items:center;justify-content:center;}
  .device--active{background:var(--yellow);}
  .pair-node{position:absolute;left:175px;width:64px;height:64px;border-radius:50%;background:var(--yellow);display:flex;align-items:center;justify-content:center;}
  .pair-label{position:absolute;left:0;right:0;text-align:center;font-size:17px;color:var(--muted);}
</style>
</head>
<body>
<div class="board">

  <!-- Timers dashboard -->
  <section class="screen screen--timers">
    <header class="app-header">
      <svg width="414" height="205" viewBox="0 0 414 205"><path d="M0 0H414V135Q207 225 0 135Z" fill="#333"/><path d="M40 155Q207 240 374 155Q207 212 40 155Z" fill="#ffc000"/></svg>
      <div class="brand">Velmaro</div>
      <div class="nav-icons">
        <div class="nav-icon"><svg width="14" height="12" viewBox="0 0 14 12"><path d="M1 4a8.5 8.5 0 0 1 12 0M3 6.5a5.5 5.5 0 0 1 8 0M5 9a2.5 2.5 0 0 1 4 0" stroke="#333" stroke-width="1.6" fill="none"/><circle cx="7" cy="10.8" r="1.1" fill="#333"/></svg></div>
        <div class="nav-icon"><svg width="12" height="10" viewBox="0 0 12 10"><path d="M0 0h3v2H0zM4.5 0h3v2h-3zM9 0h3v2H9zM0 4h3v2H0zM4.5 4h3v2h-3zM9 4h3v2H9zM0 8h3v2H0zM4.5 8h3v2h-3zM9 8h3v2H9z" fill="#333"/></svg></div>
        <div class="nav-icon"><svg width="11" height="12" viewBox="0 0 11 12"><circle cx="5.5" cy="3.2" r="3" fill="#333"/><path d="M0 12a5.5 5 0 0 1 11 0Z" fill="#333"/></svg></div>
      </div>
    </header>
    <h1 class="screen-title" style="top:232px;margin:0;font-size:24px;">Motorized sirens timers</h1>

    <div class="card" style="top:283px;height:95px;">
      <svg class="abs" style="left:22px;top:26px" width="20" height="14" viewBox="0 0 20 14"><circle cx="10" cy="7" r="2" fill="#222"/><path d="M6 3.5a5 5 0 0 0 0 7M14 3.5a5 5 0 0 1 0 7M3 1a9 9 0 0 0 0 12M17 1a9 9 0 0 1 0 12" stroke="#222" stroke-width="1.4" fill="none"/></svg>
      <div class="abs" style="left:57px;top:24px;font-family:'Roboto',sans-serif;font-weight:900;font-size:15px;color:var(--ink);">SHIFT TIMING</div>
      <div class="abs" style="left:58px;top:52px;font-size:15px;">Activate the device for shift timing</div>
      <span class="toggle" style="left:308px;top:28px;"></span>
    </div>

    <svg class="abs" style="left:55px;top:402px" width="19" height="19" viewBox="0 0 19 19"><circle cx="9.5" cy="10.5" r="6.5" stroke="#ffc000" stroke-width="1.8" fill="none"/><path d="M9.5 7v3.5h3M2 4l3-3M17 4l-3-3" stroke="#ffc000" stroke-width="1.8" fill="none"/></svg>
    <div class="abs hl" style="left:89px;top:403px;font-family:'Roboto',sans-serif;font-weight:900;font-size:15px;">SCHEDULES</div>
    <svg class="abs" style="left:346px;top:405px" width="14" height="14" viewBox="0 0 14 14"><circle cx="7" cy="7" r="7" fill="#ffc000"/><path d="M7 3.5v7M3.5 7h7" stroke="#fff" stroke-width="1.8"/></svg>

    <div class="card" style="top:445px;height:134px;">
      <div class="schedule-time">9:00 AM to 1:00 PM <span class="hl">Weekdays</span></div>
      <div class="schedule-name" style="top:46px;">1st half session</div>
      <div class="schedule-name" style="top:71px;left:25px;color:var(--yellow);">Audio: Text to speech</div>
      <div class="schedule-name" style="top:96px;left:24px;font-style:italic;color:var(--ink);">The shift has be started have a nice day</div>
      <svg class="abs alarm" style="left:304px;top:21px" width="18" height="18" viewBox="0 0 18 18"><circle cx="9" cy="10" r="6.3" stroke="#222" stroke-width="1.7" fill="none"/><path d="M9 6.5V10h3M1.5 4l3-3M16.5 4l-3-3" stroke="#222" stroke-width="1.7" fill="none"/></svg>
      <svg class="abs" style="left:308px;top:54px" width="14" height="14" viewBox="0 0 14 14"><path d="M1 13l1-4 7-7 3 3-7 7Z" fill="#222"/></svg>
    </div>

    <div class="card" style="top:600px;height:79px;">
      <div class="schedule-time">1:00 PM to 2:00 PM <span class="hl">Weekdays</span></div>
      <div class="schedule-name" style="top:45px;">Lunch Time</div>
      <svg class="abs" style="left:304px;top:18px" width="18" height="18" viewBox="0 0 18 18"><circle cx="9" cy="10" r="6.3" stroke="#222" stroke-width="1.7" fill="none"/><path d="M9 6.5V10h3M1.5 4l3-3M16.5 4l-3-3" stroke="#222" stroke-width="1.7" fill="none"/></svg>
      <svg class="abs" style="left:308px;top:50px" width="14" height="14" viewBox="0 0 14 14"><path d="M1 13l1-4 7-7 3 3-7 7Z" fill="#222"/></svg>
    </div>

    <div class="card" style="top:699px;height:79px;">
      <div class="schedule-time">4:00 PM to 4:20 PM <span class="hl">Weekdays</span></div>
      <div class="schedule-name" style="top:45px;">Coffee Break</div>
      <svg class="abs" style="left:304px;top:18px" width="18" height="18" viewBox="0 0 18 18"><circle cx="9" cy="10" r="6.3" stroke="#222" stroke-width="1.7" fill="none"/><path d="M9 6.5V10h3M1.5 4l3-3M16.5 4l-3-3" stroke="#222" stroke-width="1.7" fill="none"/></svg>
      <svg class="abs" style="left:308px;top:50px" width="14" height="14" viewBox="0 0 14 14"><path d="M1 13l1-4 7-7 3 3-7 7Z" fill="#222"/></svg>
    </div>

    <div class="card" style="top:797px;height:79px;">
      <div class="schedule-time">6:00 PM <span class="hl">Weekdays</span></div>
      <div class="schedule-name" style="top:45px;">Signing out time</div>
      <svg class="abs" style="left:304px;top:18px" width="18" height="18" viewBox="0 0 18 18"><circle cx="9" cy="10" r="6.3" stroke="#222" stroke-width="1.7" fill="none"/><path d="M9 6.5V10h3M1.5 4l3-3M16.5 4l-3-3" stroke="#222" stroke-width="1.7" fill="none"/></svg>
      <svg class="abs" style="left:308px;top:50px" width="14" height="14" viewBox="0 0 14 14"><path d="M1 13l1-4 7-7 3 3-7 7Z" fill="#222"/></svg>
    </div>

    <div class="card" style="top:896px;height:79px;">
      <div class="schedule-time">9:00 AM to 12 PM <span class="hl">Weekdays</span></div>
      <div class="schedule-name" style="top:45px;">Special Session</div>
      <svg class="abs" style="left:304px;top:18px" width="18" height="18" viewBox="0 0 18 18"><circle cx="9" cy="10" r="6.3" stroke="#222" stroke-width="1.7" fill="none"/><path d="M9 6.5V10h3M1.5 4l3-3M16.5 4l-3-3" stroke="#222" stroke-width="1.7" fill="none"/></svg>
      <svg class="abs" style="left:308px;top:50px" width="14" height="14" viewBox="0 0 14 14"><path d="M1 13l1-4 7-7 3 3-7 7Z" fill="#222"/></svg>
    </div>

    <svg class="abs" style="left:37px;top:1010px" width="14" height="16" viewBox="0 0 14 16"><path d="M7 1a4.5 4.5 0 0 1 4.5 4.5V10l2 2.5H.5L2.5 10V5.5A4.5 4.5 0 0 1 7 1Z" fill="#ffc000"/><circle cx="7" cy="14.5" r="1.5" fill="#ffc000"/></svg>
    <div class="abs hl" style="left:63px;top:1009px;font-family:'Roboto',sans-serif;font-weight:900;font-size:15px;">STATUS</div>
    <p class="abs" style="left:37px;top:1038px;width:350px;margin:0;font-size:15px;line-height:26px;">Next ring of sieren is at 1:00 PM to 2:00 PM which is lunch time (Sieren alarm in 20 mins)</p>
  </section>

  <!-- Add schedule -->
  <section class="screen screen--schedule">
    <header class="app-header">
      <svg width="414" height="205" viewBox="0 0 414 205"><path d="M0 0H414V135Q207 225 0 135Z" fill="#333"/><path d="M40 155Q207 240 374 155Q207 212 40 155Z" fill="#ffc000"/></svg>
      <div class="brand">Velmaro</div>
      <div class="nav-icons">
        <div class="nav-icon"><svg width="14" height="12" viewBox="0 0 14 12"><path d="M1 4a8.5 8.5 0 0 1 12 0M3 6.5a5.5 5.5 0 0 1 8 0M5 9a2.5 2.5 0 0 1 4 0" stroke="#333" stroke-width="1.6" fill="none"/><circle cx="7" cy="10.8" r="1.1" fill="#333"/></svg></div>
        <div class="nav-icon"><svg width="12" height="10" viewBox="0 0 12 10"><path d="M0 0h3v2H0zM4.5 0h3v2h-3zM9 0h3v2H9zM0 4h3v2H0zM4.5 4h3v2h-3zM9 4h3v2H9zM0 8h3v2H0zM4.5 8h3v2h-3zM9 8h3v2H9z" fill="#333"/></svg></div>
        <div class="nav-icon"><svg width="11" height="12" viewBox="0 0 11 12"><circle cx="5.5" cy="3.2" r="3" fill="#333"/><path d="M0 12a5.5 5 0 0 1 11 0Z" fill="#333"/></svg></div>
      </div>
    </header>
    <h1 class="screen-title" style="top:239px;margin:0;font-size:19px;">Add the new schedules for siren</h1>

    <div class="card field" style="top:287px;"><span class="field-label">Title of siren alarm</span>
      <svg class="field-icon" width="15" height="14" viewBox="0 0 15 14"><rect x="1" y="3" width="10" height="10" rx="1" stroke="#444" stroke-width="1.4" fill="none"/><path d="M6 8l1-2.5 6-5 1.5 1.5-6 5Z" fill="#444"/></svg></div>
    <div class="card field" style="top:361px;"><span class="field-label">Start time of siren</span>
      <svg class="field-icon" width="14" height="14" viewBox="0 0 14 14"><circle cx="7" cy="7" r="5.5" stroke="#444" stroke-width="1.6" fill="none"/><path d="M7 4v3.2H4.8" stroke="#444" stroke-width="1.6" fill="none"/></svg></div>
    <div class="card field" style="top:435px;"><span class="field-label">End time of siren</span>
      <svg class="field-icon" width="14" height="14" viewBox="0 0 14 14"><circle cx="7" cy="7" r="5.5" stroke="#444" stroke-width="1.6" fill="none"/><path d="M7 4v3.2H4.8" stroke="#444" stroke-width="1.6" fill="none"/></svg></div>

    <div class="abs" style="left:33px;top:521px;font-family:'Roboto',sans-serif;font-weight:900;font-size:17px;color:var(--ink);">WEEK</div>
    <div class="abs" style="left:224px;top:523px;font-size:13px;">Weekdays</div>
    <span class="toggle" style="left:297px;top:526px;"></span>
    <div class="abs" style="left:328px;top:523px;font-size:13px;">Weekend</div>

    <div class="card field" style="top:572px;"><span class="field-label">Audio Format</span>
      <svg class="field-icon" width="10" height="14" viewBox="0 0 10 14"><path d="M5 1l4 5H1ZM5 13l4-5H1Z" fill="#444"/></svg></div>
    <div class="card field" style="top:646px;"><span class="field-label">Choose audio from files</span>
      <svg class="field-icon" width="17" height="13" viewBox="0 0 17 13"><path d="M4 12a3.5 3.5 0 0 1-.3-7A5 5 0 0 1 13 4a4 4 0 0 1 0 8Z" fill="#444"/><path d="M8.5 10V6M6.5 8l2-2 2 2" stroke="#fff" stroke-width="1.3" fill="none"/></svg></div>

    <div class="btn-primary">ADD FILES</div>
  </section>

  <!-- Devices list -->
  <section class="screen screen--devices">
    <header class="app-header">
      <svg width="414" height="205" viewBox="0 0 414 205"><path d="M0 0H414V135Q207 225 0 135Z" fill="#333"/><path d="M40 155Q207 240 374 155Q207 212 40 155Z" fill="#ffc000"/></svg>
      <div class="brand">Velmaro</div>
      <div class="nav-icons">
        <div class="nav-icon"><svg width="14" height="12" viewBox="0 0 14 12"><path d="M1 4a8.5 8.5 0 0 1 12 0M3 6.5a5.5 5.5 0 0 1 8 0M5 9a2.5 2.5 0 0 1 4 0" stroke="#333" stroke-width="1.6" fill="none"/><circle cx="7" cy="10.8" r="1.1" fill="#333"/></svg></div>
        <div class="nav-icon"><svg width="12" height="10" viewBox="0 0 12 10"><path d="M0 0h3v2H0zM4.5 0h3v2h-3zM9 0h3v2H9zM0 4h3v2H0zM4.5 4h3v2h-3zM9 4h3v2H9zM0 8h3v2H0zM4.5 8h3v2h-3zM9 8h3v2H9z" fill="#333"/></svg></div>
        <div class="nav-icon"><svg width="11" height="12" viewBox="0 0 11 12"><circle cx="5.5" cy="3.2" r="3" fill="#333"/><path d="M0 12a5.5 5 0 0 1 11 0Z" fill="#333"/></svg></div>
      </div>
    </header>
    <h1 class="screen-title" style="top:239px;margin:0;font-size:19px;">Devices available to connect</h1>

    <div class="card field device--active" style="top:287px;"><span class="field-label">XYZ Timer</span><span class="toggle toggle--on" style="left:302px;top:21px;"></span></div>
    <div class="card field" style="top:361px;"><span class="field-label">IT Siren abc</span><span class="toggle" style="left:302px;top:21px;"></span></div>
    <div class="card field" style="top:435px;"><span class="field-label">Support team speaker</span><span class="toggle" style="left:302px;top:21px;"></span></div>
  </section>

  <!-- Wi-Fi pairing -->
  <section class="screen screen--pairing">
    <header class="app-header">
      <svg width="414" height="205" viewBox="0 0 414 205"><path d="M0 0H414V135Q207 225 0 135Z" fill="#333"/><path d="M40 155Q207 240 374 155Q207 212 40 155Z" fill="#ffc000"/></svg>
      <div class="brand">Velmaro</div>
      <div class="nav-icons">
        <div class="nav-icon"><svg width="14" height="12" viewBox="0 0 14 12"><path d="M1 4a8.5 8.5 0 0 1 12 0M3 6.5a5.5 5.5 0 0 1 8 0M5 9a2.5 2.5 0 0 1 4 0" stroke="#333" stroke-width="1.6" fill="none"/><circle cx="7" cy="10.8" r="1.1" fill="#333"/></svg></div>
        <div class="nav-icon"><svg width="12" height="10" viewBox="0 0 12 10"><path d="M0 0h3v2H0zM4.5 0h3v2h-3zM9 0h3v2H9zM0 4h3v2H0zM4.5 4h3v2h-3zM9 4h3v2H9zM0 8h3v2H0zM4.5 8h3v2h-3zM9 8h3v2H9z" fill="#333"/></svg></div>
        <div class="nav-icon"><svg width="11" height="12" viewBox="0 0 11 12"><circle cx="5.5" cy="3.2" r="3" fill="#333"/><path d="M0 12a5.5 5 0 0 1 11 0Z" fill="#333"/></svg></div>
      </div>
    </header>
    <h1 class="screen-title" style="top:240px;margin:0;font-size:19px;line-height:30px;">You will be connecting to<br>XYZ timer to your account using<br>Wi-Fi pairing</h1>

    <div class="pair-node" style="top:363px;"><svg width="20" height="20" viewBox="0 0 11 12"><circle cx="5.5" cy="3.2" r="3" fill="#333"/><path d="M0 12a5.5 5 0 0 1 11 0Z" fill="#333"/></svg></div>
    <div class="pair-label" style="top:437px;">abc</div>
    <svg class="abs" style="left:199px;top:476px" width="16" height="80" viewBox="0 0 16 80"><path d="M8 0v18M8 58v20" stroke="#ffc000" stroke-width="1.3" stroke-dasharray="4 4"/><circle cx="8" cy="40" r="7.5" fill="#222"/><path d="M8 35.5v8M5 40.5l3 3 3-3" stroke="#fff" stroke-width="1.6" fill="none"/></svg>
    <div class="pair-node" style="top:573px;"><svg width="20" height="20" viewBox="0 0 14 14"><circle cx="7" cy="7" r="5.5" stroke="#333" stroke-width="1.8" fill="none"/><path d="M7 4v3.2H4.8" stroke="#333" stroke-width="1.8" fill="none"/></svg></div>
    <div class="pair-label" style="top:647px;">xyz timer</div>
  </section>

</div>
</body>
</html>
```